3 out of 100 people will get deadly skin cancer - we need a great illustration that shows this!

We put together a prototype image that communicates lifetime skin cancer risk. (see attached). We are looking for illustrators who can take make a new/better/cooler graphic that communicates this idea. It could be as simple as a superior illustration of the graphic we have or illustrators can propose a completely different idea.What should the illustration communicate?U.S. adults have a lifetime risk of developing skin cancer of 1 in 5. But we don't want to show 1 in 5; we want to show that number in a larger group. For example, in the attached illustration we show 20 in 100 people get skin cancer (i.e., 100 beach towels/umbrellas and 20 of them are red). Research has shown that people are more likely to accurately understand numbers like this when you convey them for larger groups (i.e., 20 out of 100 rather than 1 out of 5). U.S. adults also have a lifetime risk of 2.3% of developing the deadliest form of skin cancer (melanoma). In other words, approximately 3 in 100 people will develop melanoma in their lifetime. Ideally, a single image will convey both lifetime skin cancer risk (20 in 100) and melanoma risk (3 in 100). We will award a top three as follows: 1st place = $300, 2nd place = $250, third place = $200. We will also buy any design beyond 3rd place that we like for $100. For example, we purchased 24 designs in our last contest on Artmarketly.This research is supported by funding from the Corvane Institute of Science.

Target Market(s)

The U.S. public; individuals at high risk of developing skin cancer

Industry/Entity Type

Medicine

Colors

Designer to choose colors to be used in the design.

Requirements
Must have
• an original illustration that conveys both lifetime risk of developing skin cancer (20 in 100) and melanoma (3 in 100).
Nice to have
• It can be beach towels and umbrellas, just like our prototype, or the designers can pitch an original idea. Imagery can be realistic or cartoonish (or something in between). It should be illustrations, though. Not edited photos. The image should be in color (no black and white illustrations).
Should not have
• Photos. Clip art. Free vector images.
• We are looking for original illustrations created by the designer.

```html
<!DOCTYPE html>
<html lang="en">
<head>
<meta charset="utf-8">
<title>Lifetime Skin Cancer Risk: 20 in 100</title>
<link rel="stylesheet" href="https://fonts.googleapis.com/css2?family=Source+Sans+3:wght@400&display=swap">
<style>
  :root {
    --legend-bg: #eef7fd;
    --page-bg: #ffffff;
    --text: #1a1a1a;
    --clear-top: #6fc3c3;
    --clear-bottom: #f6dcd8;
    --cancer-top: #e23d92;
    --cancer-bottom: #c8137a;
    --melanoma-top: #d81c7c;
    --melanoma-bottom: #e0202a;
  }
  * { box-sizing: border-box; margin: 0; padding: 0; }
  html, body {
    width: 1096px; height: 1200px; overflow: hidden;
    background: var(--page-bg);
    font-family: "Source Sans 3", sans-serif;
  }
  .risk-chart { position: relative; width: 1096px; height: 1200px; }
  .legend {
    position: absolute; left: 0; top: 0; width: 1096px; height: 172px;
    background: var(--legend-bg);
  }
  .legend-item { position: absolute; top: 48px; display: flex; align-items: center; }
  .legend-item--clear { left: 40px; }
  .legend-item--cancer { left: 416px; }
  .legend-item--melanoma { left: 780px; }
  .legend-label {
    font-size: 28px; color: var(--text); margin-left: 14px; letter-spacing: 0.2px;
  }
  .bed {
    width: 96px; height: 76px; border-radius: 8px 14px 6px 10px;
  }
  .legend .bed { width: 126px; height: 98px; }
  .bed--clear { background: linear-gradient(160deg, var(--clear-top) 0%, #b9e4e2 55%, var(--clear-bottom) 100%); }
  .bed--cancer { background: linear-gradient(160deg, var(--cancer-top) 0%, #ef7fb8 55%, var(--cancer-bottom) 100%); }
  .bed--melanoma { background: linear-gradient(160deg, var(--melanoma-top) 0%, #ee6fa6 50%, var(--melanoma-bottom) 100%); }
  .population {
    position: absolute; left: 22px; top: 204px;
    display: grid;
    grid-template-columns: repeat(10, 96px);
    grid-auto-rows: 76px;
    column-gap: 10px; row-gap: 23.5px;
  }
</style>
</head>
<body>
<main class="risk-chart">
  <header class="legend">
    <div class="legend-item legend-item--clear">
      <div class="bed bed--clear" role="img" aria-label="Illustration of an open tanning bed with a person, teal: no skin cancer"></div>
      <span class="legend-label">No skin cancer</span>
    </div>
    <div class="legend-item legend-item--cancer">
      <div class="bed bed--cancer" role="img" aria-label="Illustration of an open tanning bed with a person, magenta: skin cancer"></div>
      <span class="legend-label">Skin cancer</span>
    </div>
    <div class="legend-item legend-item--melanoma">
      <div class="bed bed--melanoma" role="img" aria-label="Illustration of an open tanning bed with a person in red, magenta: melanoma"></div>
      <span class="legend-label">Melanoma</span>
    </div>
  </header>

  <section class="population" aria-label="100 people: 20 develop skin cancer, 3 of them melanoma">
    <!-- row 1 -->
    <div class="bed bed--clear" role="img" aria-label="Tanning bed, no skin cancer"></div>
    <div class="bed bed--cancer" role="img" aria-label="Tanning bed, skin cancer"></div>
    <div class="bed bed--clear" role="img" aria-label="Tanning bed, no skin cancer"></div>
    <div class="bed bed--clear" role="img" aria-label="Tanning bed, no skin cancer"></div>
    <div class="bed bed--cancer" role="img" aria-label="Tanning bed, skin cancer"></div>
    <div class="bed bed--clear" role="img" aria-label="Tanning bed, no skin cancer"></div>
    <div class="bed bed--clear" role="img" aria-label="Tanning bed, no skin cancer"></div>
    <div class="bed bed--clear" role="img" aria-label="Tanning bed, no skin cancer"></div>
    <div class="bed bed--clear" role="img" aria-label="Tanning bed, no skin cancer"></div>
    <div class="bed bed--clear" role="img" aria-label="Tanning bed, no skin cancer"></div>
    <!-- row 2 -->
    <div class="bed bed--clear" role="img" aria-label="Tanning bed, no skin cancer"></div>
    <div class="bed bed--clear" role="img" aria-label="Tanning bed, no skin cancer"></div>
    <div class="bed bed--clear" role="img" aria-label="Tanning bed, no skin cancer"></div>
    <div class="bed bed--clear" role="img" aria-label="Tanning bed, no skin cancer"></div>
    <div class="bed bed--clear" role="img" aria-label="Tanning bed, no skin cancer"></div>
    <div class="bed bed--melanoma" role="img" aria-label="Tanning bed, melanoma"></div>
    <div class="bed bed--clear" role="img" aria-label="Tanning bed, no skin cancer"></div>
    <div class="bed bed--clear" role="img" aria-label="Tanning bed, no skin cancer"></div>
    <div class="bed bed--clear" role="img" aria-label="Tanning bed, no skin cancer"></div>
    <div class="bed bed--cancer" role="img" aria-label="Tanning bed, skin cancer"></div>
    <!-- row 3 -->
    <div class="bed bed--cancer" role="img" aria-label="Tanning bed, skin cancer"></div>
    <div class="bed bed--clear" role="img" aria-label="Tanning bed, no skin cancer"></div>
    <div class="bed bed--clear" role="img" aria-label="Tanning bed, no skin cancer"></div>
    <div class="bed bed--clear" role="img" aria-label="Tanning bed, no skin cancer"></div>
    <div class="bed bed--clear" role="img" aria-label="Tanning bed, no skin cancer"></div>
    <div class="bed bed--clear" role="img" aria-label="Tanning bed, no skin cancer"></div>
    <div class="bed bed--clear" role="img" aria-label="Tanning bed, no skin cancer"></div>
    <div class="bed bed--clear" role="img" aria-label="Tanning bed, no skin cancer"></div>
    <div class="bed bed--clear" role="img" aria-label="Tanning bed, no skin cancer"></div>
    <div class="bed bed--clear" role="img" aria-label="Tanning bed, no skin cancer"></div>
    <!-- row 4 -->
    <div class="bed bed--clear" role="img" aria-label="Tanning bed, no skin cancer"></div>
    <div class="bed bed--clear" role="img" aria-label="Tanning bed, no skin cancer"></div>
    <div class="bed bed--clear" role="img" aria-label="Tanning bed, no skin cancer"></div>
    <div class="bed bed--cancer" role="img" aria-label="Tanning bed, skin cancer"></div>
    <div class="bed bed--clear" role="img" aria-label="Tanning bed, no skin cancer"></div>
    <div class="bed bed--clear" role="img" aria-label="Tanning bed, no skin cancer"></div>
    <div class="bed bed--clear" role="img" aria-label="Tanning bed, no skin cancer"></div>
    <div class="bed bed--cancer" role="img" aria-label="Tanning bed, skin cancer"></div>
    <div class="bed bed--cancer" role="img" aria-label="Tanning bed, skin cancer"></div>
    <div class="bed bed--clear" role="img" aria-label="Tanning bed, no skin cancer"></div>
    <!-- row 5 -->
    <div class="bed bed--clear" role="img" aria-label="Tanning bed, no skin cancer"></div>
    <div class="bed bed--clear" role="img" aria-label="Tanning bed, no skin cancer"></div>
    <div class="bed bed--cancer" role="img" aria-label="Tanning bed, skin cancer"></div>
    <div class="bed bed--clear" role="img" aria-label="Tanning bed, no skin cancer"></div>
    <div class="bed bed--clear" role="img" aria-label="Tanning bed, no skin cancer"></div>
    <div class="bed bed--clear" role="img" aria-label="Tanning bed, no skin cancer"></div>
    <div class="bed bed--clear" role="img" aria-label="Tanning bed, no skin cancer"></div>
    <div class="bed bed--clear" role="img" aria-label="Tanning bed, no skin cancer"></div>
    <div class="bed bed--clear" role="img" aria-label="Tanning bed, no skin cancer"></div>
    <div class="bed bed--melanoma" role="img" aria-label="Tanning bed, melanoma"></div>
    <!-- row 6 -->
    <div class="bed bed--clear" role="img" aria-label="Tanning bed, no skin cancer"></div>
    <div class="bed bed--clear" role="img" aria-label="Tanning bed, no skin cancer"></div>
    <div class="bed bed--clear" role="img" aria-label="Tanning bed, no skin cancer"></div>
    <div class="bed bed--clear" role="img" aria-label="Tanning bed, no skin cancer"></div>
    <div class="bed bed--clear" role="img" aria-label="Tanning bed, no skin cancer"></div>
    <div class="bed bed--clear" role="img" aria-label="Tanning bed, no skin cancer"></div>
    <div class="bed bed--cancer" role="img" aria-label="Tanning bed, skin cancer"></div>
    <div class="bed bed--clear" role="img" aria-label="Tanning bed, no skin cancer"></div>
    <div class="bed bed--clear" role="img" aria-label="Tanning bed, no skin cancer"></div>
    <div class="bed bed--clear" role="img" aria-label="Tanning bed, no skin cancer"></div>
    <!-- row 7 -->
    <div class="bed bed--cancer" role="img" aria-label="Tanning bed, skin cancer"></div>
    <div class="bed bed--clear" role="img" aria-label="Tanning bed, no skin cancer"></div>
    <div class="bed bed--clear" role="img" aria-label="Tanning bed, no skin cancer"></div>
    <div class="bed bed--clear" role="img" aria-label="Tanning bed, no skin cancer"></div>
    <div class="bed bed--cancer" role="img" aria-label="Tanning bed, skin cancer"></div>
    <div class="bed bed--clear" role="img" aria-label="Tanning bed, no skin cancer"></div>
    <div class="bed bed--cancer" role="img" aria-label="Tanning bed, skin cancer"></div>
    <div class="bed bed--clear" role="img" aria-label="Tanning bed, no skin cancer"></div>
    <div class="bed bed--clear" role="img" aria-label="Tanning bed, no skin cancer"></div>
    <div class="bed bed--clear" role="img" aria-label="Tanning bed, no skin cancer"></div>
    <!-- row 8 -->
    <div class="bed bed--clear" role="img" aria-label="Tanning bed, no skin cancer"></div>
    <div class="bed bed--cancer" role="img" aria-label="Tanning bed, skin cancer"></div>
    <div class="bed bed--clear" role="img" aria-label="Tanning bed, no skin cancer"></div>
    <div class="bed bed--clear" role="img" aria-label="Tanning bed, no skin cancer"></div>
    <div class="bed bed--clear" role="img" aria-label="Tanning bed, no skin cancer"></div>
    <div class="bed bed--cancer" role="img" aria-label="Tanning bed, skin cancer"></div>
    <div class="bed bed--clear" role="img" aria-label="Tanning bed, no skin cancer"></div>
    <div class="bed bed--clear" role="img" aria-label="Tanning bed, no skin cancer"></div>
    <div class="bed bed--clear" role="img" aria-label="Tanning bed, no skin cancer"></div>
    <div class="bed bed--clear" role="img" aria-label="Tanning bed, no skin cancer"></div>
    <!-- row 9 -->
    <div class="bed bed--clear" role="img" aria-label="Tanning bed, no skin cancer"></div>
    <div class="bed bed--clear" role="img" aria-label="Tanning bed, no skin cancer"></div>
    <div class="bed bed--cancer" role="img" aria-label="Tanning bed, skin cancer"></div>
    <div class="bed bed--clear" role="img" aria-label="Tanning bed, no skin cancer"></div>
    <div class="bed bed--clear" role="img" aria-label="Tanning bed, no skin cancer"></div>
    <div class="bed bed--clear" role="img" aria-label="Tanning bed, no skin cancer"></div>
    <div class="bed bed--clear" role="img" aria-label="Tanning bed, no skin cancer"></div>
    <div class="bed bed--clear" role="img" aria-label="Tanning bed, no skin cancer"></div>
    <div class="bed bed--cancer" role="img" aria-label="Tanning bed, skin cancer"></div>
    <div class="bed bed--clear" role="img" aria-label="Tanning bed, no skin cancer"></div>
    <!-- row 10 -->
    <div class="bed bed--clear" role="img" aria-label="Tanning bed, no skin cancer"></div>
    <div class="bed bed--clear" role="img" aria-label="Tanning bed, no skin cancer"></div>
    <div class="bed bed--melanoma" role="img" aria-label="Tanning bed, melanoma"></div>
    <div class="bed bed--clear" role="img" aria-label="Tanning bed, no skin cancer"></div>
    <div class="bed bed--clear" role="img" aria-label="Tanning bed, no skin cancer"></div>
    <div class="bed bed--clear" role="img" aria-label="Tanning bed, no skin cancer"></div>
    <div class="bed bed--clear" role="img" aria-label="Tanning bed, no skin cancer"></div>
    <div class="bed bed--clear" role="img" aria-label="Tanning bed, no skin cancer"></div>
    <div class="bed bed--clear" role="img" aria-label="Tanning bed, no skin cancer"></div>
    <div class="bed bed--cancer" role="img" aria-label="Tanning bed, skin cancer"></div>
  </section>
</main>
</body>
</html>
```